Webdesign für BWT Lorenow, Spielgeräte
Zielgruppe
Die Firma BAU-WERK-TRAUM Udo Lorenow stellt individuelle Spielgeräte vor allem aus Holz her.
Zum Portfolio der Firma gehören neben der Produktion von kompletten Spielplatzausstattungen auch die Montage dieser, der Garten- und Landschaftsbau sowie ein weiterführender Service. Alle wichtigen Unternehmensbereiche befinden sich „unter einem Dach“, beginnend mit der Planung über die Produktion der Spielgeräte bis hin zur Montage vor Ort.
Aufgabenstellung
- Design als PSD
- es soll einen Relaunch der Website geben
- Bildmaterial liefert die jetzige Website - bitte hier bedienen bzw. siehe Katalog anbei
- frisch, modern
- die Sidebar mit den einzelnen Produktkategorien muss anders plaziert werden
- halten Sie sich an das neue Farbkonzept - siehe Katalog
- WICHTIG ist, dass die Produkte im Erzgebirge gefertigt werden - siehe Seite 2 aus dem Katalog

```html
<!DOCTYPE html>
<html lang="de">
<head>
<meta charset="utf-8">
<title>BWT Lorenow – Spielanlagen</title>
<link href="https://fonts.googleapis.com/css2?family=Chewy&family=Barlow:wght@300;400;500&display=swap" rel="stylesheet">
<style>
:root{
  --red:#d91f2d;
  --pink:#e5176f;
  --orange:#d9572a;
  --amber:#e48b2a;
  --lime:#d3d92c;
  --sky:#6ccbea;
  --white:#fff;
  --ink:#333;
}
*{margin:0;padding:0;box-sizing:border-box}
html,body{width:1200px;height:3000px;overflow:hidden;background:var(--white)}
body{font-family:"Barlow",Arial,sans-serif;font-weight:300;color:var(--ink)}
.page{position:relative;width:1200px;height:3000px;overflow:hidden}
.abs{position:absolute}
.display{font-family:"Chewy","Arial Rounded MT Bold","Arial Black",sans-serif;font-weight:400}

/* hero */
.hero-photo{left:0;top:0;width:1200px;height:480px;background:linear-gradient(100deg,#7b6a5a 0%,#a89b8a 35%,#e8d2c0 60%,#6f8fb8 85%,#c9b8a6 100%)}
.waves{left:0;top:0;width:1200px;height:3000px}
.logo{left:75px;top:0;width:92px;height:120px;background:var(--white);display:flex;flex-direction:column;align-items:center;justify-content:center;gap:8px;color:var(--red);font-weight:500;font-size:14px;text-align:center;line-height:1.1}
.logo-dot{width:26px;height:26px;border-radius:50%;background:var(--red)}
.nav{left:225px;top:34px;display:flex;gap:47px}
.nav a{font-family:"Chewy","Arial Rounded MT Bold","Arial Black",sans-serif;font-size:22px;color:var(--white);text-decoration:none}
.social{top:40px;width:44px;height:44px;border-radius:50%;display:flex;align-items:center;justify-content:center}
.hero-kicker{left:75px;top:196px;font-size:30px;color:var(--white);font-weight:300;letter-spacing:.3px}
.hero-title{left:75px;top:232px;font-size:66px;line-height:74px;color:var(--white)}
.hero-claim{left:960px;top:300px;width:165px;padding:10px 14px;border-radius:20px;background:var(--sky);color:var(--white);font-size:15px;font-weight:500;text-align:center;line-height:1.2}

/* categories */
.cats{left:75px;width:1050px;display:grid;grid-template-columns:repeat(12,1fr);gap:9px}
.cat{height:37px;border-radius:19px;color:var(--white);font-size:15px;font-weight:400;display:flex;align-items:center;justify-content:center;white-space:nowrap}
.w2{grid-column:span 2}
.cat.active{background:var(--white);color:var(--orange);border:1.5px solid var(--orange)}

/* slider */
.system-sub{left:0;width:1192px;top:655px;text-align:center;font-size:30px;color:var(--orange)}
.system-title{left:0;width:1170px;top:690px;text-align:center;font-size:64px;color:var(--orange)}
.slide{left:226px;top:792px;width:750px;height:488px;background:linear-gradient(180deg,#c4593a 0%,#b36a4a 35%,#d8c7a8 65%,#6a9a3a 100%)}
.arrow{width:78px;height:78px;border-radius:50%;background:var(--orange);top:996px;display:flex;align-items:center;justify-content:center}
.caption{left:226px;top:1295px;font-size:21px;color:var(--orange)}
.thumbs{left:227px;top:1410px;width:748px;height:106px;overflow:hidden;display:flex;gap:9px}
.thumb{flex:0 0 166px;height:106px}

/* offer */
.offer-photo{left:75px;top:1735px;width:450px;height:450px;border-radius:50%;background:radial-gradient(circle at 50% 40%,#8cc6c4 0%,#c8a277 45%,#8a9a4a 100%)}
.offer-title{left:600px;top:1752px;font-size:44px;color:var(--white)}
.offer-text{left:600px;color:var(--white);font-size:21px;line-height:25px;font-weight:300}
.offer-price{left:603px;top:2012px;font-size:28px;color:var(--white)}
.dot{border-radius:50%}

/* teasers */
.teaser{top:2377px;width:326px;height:326px;border-radius:50%}
.teaser-label{color:var(--white);font-size:34px;line-height:36px;text-align:center;width:326px}
.catalog-cover{left:152px;top:2345px;width:160px;height:215px;transform:rotate(4deg);background:linear-gradient(180deg,#e9b36a 0%,#c83a4a 55%,#d82030 100%)}
.teaser-kicker{left:437px;top:2420px;width:326px;text-align:center;color:var(--white);font-size:24px;font-weight:300}

/* footer */
.footer-line{left:0;width:1200px;text-align:center;color:var(--white);font-weight:400}
</style>
</head>
<body>
<div class="page">

  <div class="abs hero-photo" role="img" aria-label="Foto: lachendes Kleinkind mit Basecap auf einem Spielplatz"></div>

  <svg class="abs waves" viewBox="0 0 1200 3000" aria-hidden="true">
    <path d="M0,0 H1200 V182 C1100,150 1000,92 850,98 C700,104 640,168 500,152 C350,136 160,44 0,30 Z" fill="var(--red)"/>
    <path d="M0,470 C200,440 420,418 620,452 C820,486 1000,462 1200,430 V482 H0 Z" fill="var(--white)"/>
    <path d="M0,1745 C300,1690 500,1640 720,1648 C920,1656 1060,1662 1200,1650 V2312 C1000,2276 820,2262 620,2288 C420,2314 200,2262 0,2160 Z" fill="var(--pink)"/>
    <path d="M0,2878 C280,2830 500,2790 720,2800 C920,2810 1060,2846 1200,2856 V3000 H0 Z" fill="var(--red)"/>
  </svg>

  <div class="abs logo"><span class="logo-dot"></span>BWT Lorenow</div>

  <nav class="abs nav">
    <a>Spielanlagen</a><a>Aktuelles</a><a>Über uns</a><a>Shop</a>
  </nav>

  <div class="abs social" style="left:975px;background:var(--sky)"></div>
  <div class="abs social" style="left:1028px;background:var(--amber)">
    <svg width="20" height="16" viewBox="0 0 20 16"><rect x="1" y="1" width="18" height="14" rx="2" fill="none" stroke="#fff" stroke-width="1.8"/><path d="M1.5 2 L10 9 L18.5 2" fill="none" stroke="#fff" stroke-width="1.8"/></svg>
  </div>
  <div class="abs social" style="left:1081px;background:var(--lime)">
    <svg width="20" height="20" viewBox="0 0 24 24"><path d="M6.6 10.8c1.4 2.8 3.8 5.1 6.6 6.6l2.2-2.2c.3-.3.7-.4 1-.2 1.1.4 2.3.6 3.6.6.6 0 1 .4 1 1V20c0 .6-.4 1-1 1C10.6 21 3 13.4 3 4c0-.6.4-1 1-1h3.5c.6 0 1 .4 1 1 0 1.3.2 2.5.6 3.6.1.3 0 .7-.2 1z" fill="#fff"/></svg>
  </div>

  <div class="abs hero-kicker">SPIELANLAGEN VON BAU WERK TRAUM</div>
  <h1 class="abs hero-title display">Lassen Kinderaugen<br>strahlen!</h1>
  <div class="abs hero-claim">Handwerk aus dem Erzgebirge</div>

  <div class="abs cats" style="top:505px">
    <div class="cat active">Tetra</div>
    <div class="cat" style="background:#8b2a3f">Rauta</div>
    <div class="cat" style="background:#d4245e">Robinie</div>
    <div class="cat" style="background:#c8296a">Stahl</div>
    <div class="cat" style="background:#8e2c8c">Klein-Kid</div>
    <div class="cat w2" style="background:#4b3a93">Spielhäuser</div>
    <div class="cat" style="background:#1f74b6">Schaukeln</div>
    <div class="cat w2" style="background:#71c6e9">Klettergeräte</div>
    <div class="cat w2" style="background:#15a08a">Motorikparcours</div>
  </div>
  <div class="abs cats" style="top:552px">
    <div class="cat w2" style="background:#17945a">Federwippen</div>
    <div class="cat" style="background:#2a6a47">Rutschen</div>
    <div class="cat w2" style="background:#d3d92c">Sonnenschutzanlagen</div>
    <div class="cat" style="background:#d8c832">Sitzmöbel</div>
    <div class="cat w2" style="background:#e8942a">Kunststoff</div>
    <div class="cat w2" style="background:#de5a27">Fallschutz</div>
    <div class="cat w2" style="background:#bf3a24">Klanginstrumente</div>
  </div>

  <div class="abs system-sub">Spielanlagen-System</div>
  <h2 class="abs system-title display">TETRA</h2>

  <div class="abs slide" role="img" aria-label="Foto: Spielanlage im Feuerwehr-Stil mit Rutsche auf Sandfläche vor Wohnhäusern"></div>
  <div class="abs arrow" style="left:187px">
    <svg width="30" height="36" viewBox="0 0 30 36"><path d="M21 4 L8 18 L21 32" fill="none" stroke="#fff" stroke-width="7" stroke-linecap="round" stroke-linejoin="round"/></svg>
  </div>
  <div class="abs arrow" style="left:936px">
    <svg width="30" height="36" viewBox="0 0 30 36"><path d="M9 4 L22 18 L9 32" fill="none" stroke="#fff" stroke-width="7" stroke-linecap="round" stroke-linejoin="round"/></svg>
  </div>
  <div class="abs caption">Tetra Spielanlage Themenspielplatz „Alte Feuerwache“ in Talberg</div>

  <div class="abs thumbs">
    <div class="thumb" role="img" aria-label="Foto: Spielturm mit Kletterwand" style="background:linear-gradient(180deg,#9cc3e0,#c4583a 55%,#8a6a4a)"></div>
    <div class="thumb" role="img" aria-label="Foto: Spielanlage mit Brücke auf rotem Boden" style="background:linear-gradient(180deg,#dbe6ef,#d88a4a 50%,#c43a32)"></div>
    <div class="thumb" role="img" aria-label="Foto: bunte Spielanlage vor Altbauten" style="background:linear-gradient(180deg,#e6d6b8,#d8572a 50%,#3a62b0)"></div>
    <div class="thumb" role="img" aria-label="Foto: Spielturm mit roter Rutsche" style="background:linear-gradient(180deg,#8cb85a,#e0703a 55%,#6a9a3a)"></div>
    <div class="thumb" role="img" aria-label="Foto: Spielanlage" style="background:linear-gradient(180deg,#5a7a4a,#c4583a)"></div>
  </div>

  <div class="abs offer-photo" role="img" aria-label="Foto: Robinien-Spielhaus mit hellblauem Dach im Sand"></div>
  <h2 class="abs offer-title display">Angebot des Monats</h2>
  <div class="abs offer-text" style="top:1802px;font-weight:400">Robinien-Spielhaus „Wiesental“</div>
  <div class="abs offer-text" style="top:1850px;left:603px">
    - aus Robinie splintfrei geschliffen<br>
    - natürlich gewachsen<br>
    - Verbindungselemente aus Edelstahl<br>
    - gefertigt nach DIN 1176/Teil1<br>
    - Abmessungen: ca.: 1,25×1,25×1,60 m
  </div>
  <div class="abs offer-price display">Kosten: 2.850,– € netto</div>
  <div class="abs offer-text" style="top:2067px;left:603px">
    - inkl. Versand (Deutschland Festland)<br>
    - Abladetechnik muss vorhanden sein<br>
    - Lieferung komplett montiert<br>
    - Lieferzeit 4 – 6 Wochen
  </div>

  <div class="abs dot" style="left:960px;top:2200px;width:110px;height:110px;background:var(--sky)"></div>

  <div class="abs teaser" style="left:75px;background:var(--lime)"></div>
  <div class="abs catalog-cover" role="img" aria-label="Katalog-Titelblatt mit lachenden Kindern"></div>
  <div class="abs teaser-label display" style="left:75px;top:2580px">Katalog<br>herunterladen</div>

  <div class="abs teaser" style="left:437px;background:var(--sky)"></div>
  <div class="abs teaser-kicker">europaweite Lieferung</div>
  <svg class="abs" style="left:437px;top:2377px" width="326" height="326" viewBox="0 0 326 326" aria-hidden="true">
    <g fill="#fff">
      <rect x="106" y="107" width="76" height="62" rx="6"/>
      <path d="M186 124 H208 L224 146 V169 H186 Z"/>
      <circle cx="136" cy="172" r="12" fill="var(--sky)"/><circle cx="136" cy="172" r="8"/>
      <circle cx="192" cy="172" r="12" fill="var(--sky)"/><circle cx="192" cy="172" r="8"/>
    </g>
  </svg>
  <div class="abs teaser-label display" style="left:437px;top:2600px">Zum Shop</div>

  <div class="abs teaser" style="left:800px;background:var(--amber)"></div>
  <svg class="abs" style="left:908px;top:2470px" width="110" height="86" viewBox="0 0 110 86" aria-hidden="true">
    <rect x="4" y="4" width="102" height="78" rx="10" fill="none" stroke="#fff" stroke-width="8"/>
    <path d="M10 14 L55 48 L100 14" fill="none" stroke="#fff" stroke-width="8" stroke-linejoin="round"/>
  </svg>
  <div class="abs teaser-label display" style="left:800px;top:2600px">Kontakt</div>

  <div class="abs dot" style="left:80px;top:2815px;width:80px;height:80px;background:var(--sky)"></div>

  <footer>
    <div class="abs footer-line" style="top:2908px;font-size:14px">BAU-WERK-TRAUM Udo Lorenow &nbsp;|&nbsp; Werkstraße 5 &nbsp;|&nbsp; 09999 Holzhausen &nbsp;|&nbsp; Tel. 037300 - 100200 &nbsp;|&nbsp; Fax 037300 - 100201 &nbsp;|&nbsp; info@bwt-lorenow.de</div>
    <div class="abs footer-line" style="top:2935px;font-size:13px">Kontakt &nbsp;|&nbsp; Impressum &nbsp;|&nbsp; Datenschutz</div>
  </footer>
</div>
</body>
</html>
```